Energy Company 8-page Brochure

We are in need of a redesign of our 8-page brochure. Attached is the initial design that does not represent us very well. We are looking for CLEAN/CORPORATE look with a little bit of flair (graphs/charts if applicable).

I prefer white background and our company colors (blue/green) to be the accent colors. Feel free to add additional accent colors to highlight certain areas.

We are in the energy field (not just solar), so please consider the types of images that you will use. Are headquarters is located in Chicago, IL so a great looking picture of the skyline or something similar would work for the front and back cover.

We have additional marketing collateral that we will want to be uniformed once we have the right design.

Good luck, and we look forward to receiving some great designs!

Best Regards,
Kurt

Target Market(s)

Small to large businesses (B2B).

Industry/Entity Type

It Company

Colors
ffffff
9bcb3c
0255a3

Requirements
Must have
• Clean design, company colors, specified content and editable files.
Nice to have
• Graphs, charts, highlighted areas where necessary.
Should not have
• Clutter! Please utilized page space appropriately. There is a lot of content, so you need to consider graphics and image placement.

```html
<!DOCTYPE html>
<html lang="en">
<head>
<meta charset="utf-8">
<title>Everything Energy – Brochure Spreads</title>
<link href="https://fonts.googleapis.com/css2?family=Roboto+Condensed:wght@300;400;700&family=Roboto:wght@300;400;700&display=swap" rel="stylesheet">
<style>
:root{
  --bg:#cbc5c3;
  --white:#ffffff;
  --green:#5a9e3a;
  --lime:#9bcb3c;
  --blue:#0255a3;
  --navy:#1f4f8c;
  --ink:#4a4a4a;
  --rule:#8c8c8c;
  --head:"Roboto Condensed",Arial,sans-serif;
  --body:"Roboto",Arial,sans-serif;
}
*{box-sizing:border-box;margin:0;padding:0}
html,body{width:1200px;height:602px;overflow:hidden}
body{background:var(--bg);position:relative;font-family:var(--body);color:var(--ink)}
.page{position:absolute;background:var(--white);overflow:hidden;box-shadow:0 2px 6px rgba(0,0,0,.18)}

/* Cover */
.cover{left:50px;top:58px;width:250px;height:500px}
.cover-photo{position:absolute;inset:0 0 70px 0;
  background:linear-gradient(180deg,#5b7fb3 0%,#a38bb0 20%,#e8a27a 34%,#6f7f9a 48%,#3d4a63 66%,#7d95b8 82%,#ffffff 100%)}
.cover-lines{position:absolute;left:18px;top:16px;font:400 10.5px/15px var(--body);color:var(--white)}
.cover-kicker{position:absolute;left:12px;top:330px;font:300 32px/1 var(--head);color:rgba(255,255,255,.85);letter-spacing:1px}
.cover-title{position:absolute;left:8px;top:352px;font:700 78px/1 var(--head);color:var(--white);letter-spacing:-1px}
.cover-brands{position:absolute;left:0;right:0;bottom:16px;display:flex;justify-content:center;align-items:center;gap:10px}
.brand{display:flex;align-items:center;gap:4px;font:700 9px/1.1 var(--head);color:var(--blue)}
.brand .dot{width:12px;height:12px;border-radius:50%;background:var(--lime)}
.brand-divider{width:1px;height:26px;background:var(--rule)}
.brand.partner{color:var(--green)}

/* Success stories page */
.stories{left:437px;top:70px;width:346px;height:460px}
.stories-header{height:113px;background:var(--green);color:var(--white);padding:30px 0 0 24px}
.stories-header .eyebrow{font:300 17px/1 var(--head)}
.stories-header h1{font:700 40px/1 var(--head);margin-top:4px}
.story-list{list-style:none;position:absolute;left:25px;top:119px;width:297px}
.story{display:flex;align-items:center;height:41px;border:1px solid var(--rule);margin-bottom:8px;padding:3px}
.story .figure{flex:0 0 38px;height:33px;display:flex;align-items:center;justify-content:center;color:var(--white);font:700 7px/1 var(--body)}
.story.blue .figure{background:var(--navy)}
.story.green .figure{background:var(--green)}
.story p{padding:0 10px;font:400 7.5px/1.45 var(--body)}
.story strong{color:var(--green);font-weight:700}
.page-foot{position:absolute;left:20px;right:20px;bottom:10px;display:flex;justify-content:space-between;font:400 6px/1 var(--body);color:var(--rule)}
.page-foot .mark{color:var(--blue)}

/* Mission page */
.mission{left:812px;top:70px;width:338px;height:460px}
.mission-photo{position:absolute;left:0;top:0;width:338px;height:165px;
  background:linear-gradient(180deg,#0d1624 0%,#1c2a40 45%,#3a3a3f 70%,#1a1e26 100%)}
.mission-banner{position:absolute;left:15px;top:92px}
.mission-banner .eyebrow{display:inline-block;background:var(--blue);color:var(--white);font:400 15px/1 var(--head);padding:4px 6px 3px}
.mission-banner h2{font:700 21px/1.05 var(--head);color:var(--white)}
.mission-banner h2 span{display:inline-block;background:var(--blue);padding:3px 6px}
.mission-intro{position:absolute;left:18px;top:186px;width:130px;font:700 10px/1.2 var(--head);color:var(--blue)}
.mission-intro .name{display:flex;align-items:center;gap:4px;font:700 13px/1.05 var(--head);color:var(--blue);margin-bottom:4px}
.mission-intro .name .dot{flex:0 0 14px;height:14px;border-radius:50%;background:var(--lime)}
.mission-intro .name.partner{color:var(--green);margin-top:4px}
.mission-intro p{font:italic 400 9px/1.2 var(--head);color:var(--blue)}
.mission-art{position:absolute;left:148px;top:172px;width:170px;height:110px;
  background:linear-gradient(160deg,#f3f3f3 0%,#cfd3cf 55%,#a9b2a8 100%)}
.mission-body{position:absolute;left:18px;top:310px;width:302px;display:flex;gap:10px;font:400 5.4px/1.45 var(--body);color:var(--ink)}
.mission-body div{flex:1}
</style>
</head>
<body>

<section class="page cover">
  <div class="cover-photo" role="img" aria-label="Chicago skyline at sunset reflected on the lake"></div>
  <div class="cover-lines">
    We manage pricing volatility.<br>
    We mitigate risk.<br>
    We secure the lowest cost.<br>
    We lower energy usage.<br>
    We reflect your energy values.
  </div>
  <div class="cover-kicker">EVERYTHING</div>
  <div class="cover-title">ENERGY</div>
  <div class="cover-brands">
    <div class="brand"><span class="dot"></span>Brightline<br>Power</div>
    <span class="brand-divider"></span>
    <div class="brand partner">Verde Efficiency<br>Group</div>
  </div>
</section>

<section class="page stories">
  <header class="stories-header">
    <div class="eyebrow">Lower Energy Cost</div>
    <h1>Success Stories</h1>
  </header>
  <ul class="story-list">
    <li class="story blue"><span class="figure">$400,000</span><p><strong>3 YEAR SAVINGS</strong> for early learning centers by securing a low rate per kilowatt hour (kWh) for their electricity</p></li>
    <li class="story green"><span class="figure">50%</span><p><strong>50% SAVINGS</strong> for manufacturing firm by upgrading to LED lighting</p></li>
    <li class="story blue"><span class="figure">27%</span><p><strong>27% ENERGY USAGE</strong> reduction by implementing our L Series lighting controls for a Fortune 100 company</p></li>
    <li class="story green"><span class="figure">$200,000</span><p><strong>SAVINGS FOR</strong> restaurant group on their electricity bills by competitive supplier bidding</p></li>
    <li class="story blue"><span class="figure">30%</span><p><strong>30% ANNUAL SAVINGS</strong> for Distribution Center through lighting retrofit and HVAC controls</p></li>
    <li class="story green"><span class="figure">25%</span><p><strong>25% REDUCTION</strong> in water usage for a property management company for their multi-unit buildings</p></li>
  </ul>
  <footer class="page-foot"><span>01</span><span class="mark">Brightline Power</span></footer>
</section>

<section class="page mission">
  <div class="mission-photo" role="img" aria-label="Chicago river and skyline at night"></div>
  <div class="mission-banner">
    <span class="eyebrow">Our Mission Is Simple:</span>
    <h2><span>We Help Our Clients</span><br><span>Lower Their Energy Costs</span></h2>
  </div>
  <div class="mission-intro">
    <div class="name"><span class="dot"></span>Brightline Power</div>
    <p>and its partner company,</p>
    <div class="name partner">Verde Efficiency Group</div>
    <p>are dedicated to helping you lower your company's operating expenses.</p>
  </div>
  <div class="mission-art" role="img" aria-label="Stacks of banknotes descending with a blue downward arrow"></div>
  <div class="mission-body">
    <div>BRIGHTLINE POWER AND VEG are operating divisions of Summit Crest Holdings, a publicly traded energy services company. As a vendor-independent company, there are many ways in which we help you lower your energy expenditures. Brightline Power (BLP) lowers the cost of energy through competitive supplier bidding and VEG creates comprehensive energy savings solutions through the implementation of energy reduction services.</div>
    <div>OUR DIVERSE PORTFOLIO of leading competitive energy suppliers, comprehensive energy efficiency solutions, best-in-class products, and unparalleled industry experience provide our clients with the confidence that they are getting the best solutions for their energy needs.<br>BY REDUCING THE PRICE for energy and lowering usage, BLP and VEG allow businesses to keep more of their own capital.</div>
  </div>
  <footer class="page-foot"><span>02</span><span class="mark">Brightline Power</span></footer>
</section>

</body>
</html>
```